Email Banner for Technology Company

We need a new email banner. The purpose of the email banner is to make us look more professional as a business and keep all communications with clients uniform. The previous designs which we have included below have now become outdated as our brand has developed and we need the new banner to become more aligned and modern.

We are a marketing organization that specialises in lead generation, email newsletters are sent to prospects on a regular basis. Therefore, it is important that we have an aesthetically pleasing banner as this is the first real impression prospects have our business. First impressions matter.

We are looking for a new email banner design as the current design is now outdated and does not reflect who we are as a business.

The new banners are required for launch at the start of Q2.

There is future work in the pipeline for the winning design. We have multiple industry sites that will require the new design as well as creating each of these in multiple languages.

The design must include the Zevomarkly wording the tagline 'The Ultimate Research Library for Technology Pro's.
It needs to be creative and fun but still remain professional, sticking with the colour theme that already exists.

Requirements
Must have
• The design must include the Zevomarkly wording the tagline 'The Ultimate Research Library for Technology Pro's.

```html
<!DOCTYPE html>
<html lang="en">
<head>
<meta charset="utf-8">
<title>Zevomarkly Email Banner</title>
<link href="https://fonts.googleapis.com/css2?family=Roboto+Condensed:wght@300;400;700&display=swap" rel="stylesheet">
<style>
  :root {
    --page-grey: #f1f2f2;
    --sky: #b5e0f4;
    --sky-light: #c8e8f6;
    --sky-pale: #d6eef9;
    --banner-blue: #6ccbf2;
    --banner-deep: #27b6ec;
    --banner-mid: #4fc1ef;
    --brand-blue: #1aa6e0;
    --white: #ffffff;
  }
  html, body {
    margin: 0;
    padding: 0;
    width: 1200px;
    height: 462px;
    overflow: hidden;
    background: var(--page-grey);
  }
  .email-banner {
    display: block;
    width: 1200px;
    height: 462px;
    font-family: "Roboto Condensed", Arial, sans-serif;
  }
  .page-grey { fill: var(--page-grey); }
  .sky-band { fill: var(--sky); }
  .sky-shape { fill: var(--sky-light); }
  .sky-shape--pale { fill: var(--sky-pale); }
  .sky-outline { fill: none; stroke: var(--white); stroke-opacity: .55; stroke-width: 3; }
  .frame { fill: var(--white); }
  .header-fill { fill: var(--banner-blue); }
  .header-shape { fill: var(--banner-mid); }
  .header-shape--deep { fill: var(--banner-deep); }
  .header-shape--light { fill: #8fd7f5; }
  .header-outline { fill: none; stroke: var(--white); stroke-opacity: .7; stroke-width: 1.2; }
  .wordmark {
    fill: var(--white);
    font-weight: 700;
    font-size: 34px;
  }
  .click-tab { fill: var(--white); }
  .click-label {
    fill: var(--brand-blue);
    font-weight: 700;
    font-size: 11px;
    letter-spacing: .5px;
  }
  .tagline {
    fill: var(--brand-blue);
    font-size: 15px;
    font-weight: 300;
  }
  .tagline-strong { font-weight: 700; }
  .tagline-rule { stroke: var(--brand-blue); stroke-width: 1.6; }
</style>
</head>
<body>
<svg class="email-banner" viewBox="0 0 1000 385" xmlns="http://www.w3.org/2000/svg">
  <!-- page backdrop -->
  <rect class="page-grey" x="0" y="0" width="1000" height="385"/>
  <rect class="sky-band" x="0" y="30" width="1000" height="327"/>

  <!-- backdrop geometry -->
  <polygon class="sky-shape" points="0,30 560,30 440,357 0,357"/>
  <polygon class="sky-shape--pale" points="0,30 300,30 250,120 0,120"/>
  <polygon class="sky-shape" points="700,95 1000,95 1000,357 600,357"/>
  <polygon class="sky-outline" points="480,70 1000,70 1000,72 455,120"/>
  <polygon class="sky-outline" points="410,270 520,270 460,350 360,350"/>
  <polygon class="sky-outline" points="900,280 1000,250 1000,357 880,357"/>

  <!-- banner frame -->
  <rect class="frame" x="101" y="115" width="798" height="156"/>
  <rect class="header-fill" x="105" y="119" width="790" height="93"/>
  <polygon class="header-fill" points="105,212 150,212 105,242"/>

  <!-- header geometry -->
  <polygon class="header-shape--light" points="500,132 620,132 590,212 470,212"/>
  <polygon class="header-shape" points="660,140 810,140 780,212 630,212"/>
  <polygon class="header-shape--deep" points="620,172 718,172 704,212 598,212"/>
  <polygon class="header-outline" points="625,132 812,132 784,204 598,204"/>
  <polygon class="header-outline" points="588,155 658,155 648,186 578,186"/>
  <polygon class="header-outline" points="772,180 860,180 846,212 758,212"/>

  <!-- brand name -->
  <text class="wordmark" x="150" y="178">Zevomarkly</text>

  <!-- call to action tab -->
  <polygon class="click-tab" points="826,158 895,158 895,180 818,180"/>
  <text class="click-label" x="839" y="173">CLICK</text>

  <!-- tagline -->
  <text class="tagline" x="453" y="247" textLength="420" lengthAdjust="spacingAndGlyphs">THE ULTIMATE RESEARCH LIBRARY <tspan class="tagline-strong">FOR TECHNOLOGY PRO'S</tspan></text>
  <line class="tagline-rule" x1="740" y1="251" x2="829" y2="251"/>
</svg>
</body>
</html>
```